New Business Cards for MB&LR

We need updated business cards for a staff of 15 engineers, estimators, project managers, and sales people. We have recently begun changes to our website and marketing material to improve our look and branding. We are an established fabricator specializing in pressure vessels, tanks, and structural steel. The owners require us to use the existing logo and old english text design. Also, we prefer dark grey or mostly black cards.
Target Market(s)
Engineers, purchasing agents, estimators, and project managers of; mining companies, refineries, industrial construction professionals
Industry/Entity Type
Business
Contact Information for Business Card
Logo, phone, website, email, etc.
Look and feel

```html
<!DOCTYPE html>
<html lang="en">
<head>
<meta charset="utf-8">
<title>MB&amp;LR Business Cards</title>
<link rel="stylesheet" href="https://fonts.googleapis.com/css2?family=Open+Sans:wght@400;600&display=swap">
<style>
  :root {
    --stage: #2b2b2b;
    --card: #0b0b0b;
    --card-edge: #1a1a1a;
    --silver: #c9c9c9;
    --silver-dim: #8e8e8e;
    --rule: #333333;
    --text: #bdbdbd;
    --name: #e6e6e6;
  }
  * { box-sizing: border-box; margin: 0; padding: 0; }
  html, body { width: 1200px; height: 716px; overflow: hidden; }
  body {
    background: var(--stage);
    font-family: "Open Sans", Arial, sans-serif;
    display: flex;
    align-items: center;
    justify-content: center;
    gap: 60px;
  }
  .card {
    position: relative;
    width: 520px;
    height: 300px;
    background: var(--card);
    border: 1px solid var(--card-edge);
    box-shadow: 0 10px 30px rgba(0,0,0,.5);
    overflow: hidden;
  }
  .card--front { border-bottom: 6px solid var(--silver); }
  .brand-mark {
    display: flex;
    align-items: center;
    gap: 8px;
    color: var(--silver);
    font-family: "Open Sans", Arial, sans-serif;
    font-weight: 600;
    letter-spacing: 1px;
  }
  .brand-mark__square {
    width: 12px; height: 12px;
    background: var(--silver);
  }
  .card--front .brand-mark {
    position: absolute;
    top: 38px; right: 70px;
    font-size: 22px;
  }
  .divider {
    position: absolute;
    left: 30px; right: 60px;
    top: 146px;
    height: 1px;
    background: var(--rule);
  }
  .address {
    position: absolute;
    right: 28px; top: 158px;
    text-align: right;
    color: var(--text);
    font-size: 11px;
    font-style: normal;
    line-height: 1.5;
  }
  .person {
    position: absolute;
    left: 30px; top: 160px;
  }
  .person__name { color: var(--name); font-size: 15px; font-weight: 600; line-height: 20px; }
  .person__title { color: var(--silver-dim); font-size: 10px; line-height: 14px; margin-bottom: 8px; }
  .contacts { list-style: none; }
  .contacts li {
    display: flex; align-items: center; gap: 7px;
    color: var(--text); font-size: 11px; line-height: 16px;
  }
  .contacts svg { width: 9px; height: 9px; fill: var(--silver-dim); }
  .card--back {
    display: flex;
    flex-direction: column;
    align-items: center;
    justify-content: center;
    gap: 20px;
  }
  .card--back .brand-mark { font-size: 30px; }
  .company-name {
    font-family: "Open Sans", Arial, sans-serif;
    font-weight: 400;
    color: var(--silver);
    font-size: 19px;
    letter-spacing: .5px;
  }
</style>
</head>
<body>
  <section class="card card--front">
    <div class="brand-mark"><span class="brand-mark__square"></span>MB&amp;LR</div>
    <div class="divider"></div>
    <address class="address">480 East 200 South<br>Riverton Flats, UT 84000</address>
    <div class="person">
      <p class="person__name">Alan Reyes</p>
      <p class="person__title">President</p>
      <ul class="contacts">
        <li><svg viewBox="0 0 10 10"><path d="M2 0h2l1 3-1.5 1a6 6 0 0 0 2.5 2.5L7 5l3 1v2a2 2 0 0 1-2 2A8 8 0 0 1 0 2a2 2 0 0 1 2-2z"/></svg>801.555.0142</li>
        <li><svg viewBox="0 0 10 10"><rect x="1" y="0" width="8" height="10" rx="1.5"/></svg>801.555.0187</li>
        <li><svg viewBox="0 0 10 10"><path d="M0 2h10v6H0zM0 2l5 3.5L10 2"/></svg>alan@mbandlr.com</li>
        <li><svg viewBox="0 0 10 10"><circle cx="5" cy="5" r="5"/></svg>www.mbandlr.com</li>
      </ul>
    </div>
  </section>

  <section class="card card--back">
    <div class="brand-mark"><span class="brand-mark__square"></span>MB&amp;LR</div>
    <p class="company-name">Mountain Beam &amp; Load Rig Works</p>
  </section>
</body>
</html>
```